New Business Card Design Project

Make a kick ass business card for The Otter Tea Mug, using the designs. I also might like the 2nd place design logo on the back? Maybe all black with that? Not sure. Also, I'm cool with it being on metal, plastic, glass? or whatever for the business card. Maybe shaped like a shark? Let me know what else you need? Would like designs in the next day or so. Thank you.
Target Market(s)
Anyone that is cool
Contact Information for Business Card
Name: Dorian Fenwick
Phone: 317.594.8126
inventor/creator/entrepreneur/owner
www.theottertyeamug.example
social media links
https://www.facebook.com/theottertyeamug
https://twitter.com/otter_brew
https://www.instagram.com/theottertyeamug/
I'll get the Pinterest one soon
Colors
Designer to choose colors to be used in the design.
Requirements
Must have
- The Otter Tea Mug
- www.theottertyeamug.example
- social media tags?
- My logos and picture/photo of wine glass
Nice to have
- Maybe shaped like a wine glass or shark
- I'll let you decide but my same colors from my website would be nice

```html
<!DOCTYPE html>
<html lang="en">
<head>
<meta charset="utf-8">
<title>The Otter Tea Mug — Business Card</title>
<link rel="stylesheet" href="https://fonts.googleapis.com/css2?family=Montserrat:wght@300;400;600;700&display=swap">
<style>
  :root {
    --backdrop: #e8e3db;
    --brand-red: #b03b43;
    --band-red: #b43b46;
    --band-red-deep: #a8343f;
    --card-white: #f6f6f4;
    --ink-grey: #6b6b6d;
    --on-red: #ffffff;
    --mark-red: #a83244;
    --mark-plum: #8c3a55;
  }
  * { box-sizing: border-box; margin: 0; padding: 0; }
  html, body { width: 900px; height: 1200px; overflow: hidden; }
  body {
    background: var(--backdrop);
    font-family: "Montserrat", Arial, sans-serif;
    position: relative;
  }
  .card {
    position: absolute;
    left: 78px;
    width: 762px;
    height: 432px;
    border-radius: 22px;
    overflow: hidden;
  }
  .card-front { top: 137px; background: var(--brand-red); color: var(--on-red); }
  .card-back { top: 632px; background: var(--card-white); }

  .holder-name {
    position: absolute; top: 54px; width: 100%;
    text-align: center; font-weight: 700; font-size: 30px; letter-spacing: 0.3px;
  }
  .holder-role {
    position: absolute; top: 92px; width: 100%;
    text-align: center; font-weight: 400; font-size: 23px;
  }
  .mascot-art {
    position: absolute; border-radius: 60px 12px 60px 12px;
  }
  .card-front .mascot-art {
    left: 177px; top: 138px; width: 408px; height: 146px;
    background: linear-gradient(90deg, rgba(255,255,255,0.5), rgba(255,255,255,0.85) 55%, rgba(255,255,255,0.5));
  }
  .card-back .mascot-art {
    left: 202px; top: 32px; width: 366px; height: 134px;
    background: linear-gradient(90deg, var(--mark-plum), var(--mark-red) 55%, var(--mark-plum));
    opacity: 0.85;
  }
  .contact {
    position: absolute; top: 306px; width: 100%;
    text-align: center; font-size: 22px; line-height: 29px; list-style: none;
  }
  .contact .email { font-weight: 600; }

  .wordmark {
    position: absolute; top: 196px; width: 100%;
    text-align: center; font-weight: 300; font-size: 78px;
    color: var(--ink-grey); letter-spacing: -0.5px;
  }
  .social-band {
    position: absolute; left: 0; bottom: 0; width: 100%; height: 132px;
    background: linear-gradient(180deg, var(--band-red), var(--band-red-deep));
    display: flex; align-items: center; justify-content: space-between;
    padding: 0 60px 0 36px; color: var(--on-red); list-style: none;
  }
  .social-handle { display: flex; align-items: center; gap: 16px; font-size: 21px; font-weight: 400; }
  .social-dot { width: 34px; height: 34px; border-radius: 50%; background: var(--on-red); flex: none; }
</style>
</head>
<body>
  <section class="card card-front">
    <h1 class="holder-name">Dorian Fenwick</h1>
    <p class="holder-role">Inventor/Creator/Entrepreneur/Owner</p>
    <div class="mascot-art" role="img" aria-label="Brand mascot illustration made of white dots"></div>
    <ul class="contact">
      <li class="phone">317.594.8126</li>
      <li class="email">email@theottertyeamug.example</li>
      <li class="web">www.theottertyeamug.example</li>
    </ul>
  </section>

  <section class="card card-back">
    <div class="mascot-art" role="img" aria-label="Brand mascot illustration made of red and plum dots"></div>
    <h2 class="wordmark">OtterTeaMug</h2>
    <ul class="social-band">
      <li class="social-handle"><span class="social-dot"></span>theottertyeamug</li>
      <li class="social-handle"><span class="social-dot"></span>otter_brew</li>
      <li class="social-handle"><span class="social-dot"></span>otterbrew</li>
    </ul>
  </section>
</body>
</html>
```